Korean Homemade food restaurant just like what your mom cooks at home

I need a black and white simple and modern design according to my logo.
My restaurant name is Nal Som (meaning of home cooking).
I need to have 늘찬(Nal Som) in Korean need to be included. Once again 늘찬.
I am not sure if I need to include my name and number and adress.
Updates

늘찬 Nal Som 478 Harwell Rd. Clarksville, TN 37118 Mark Yoon Owner Cell:931-608-2913 Store:931-617-3084

Target Market(s)

business owners, university students

Industry/Entity Type

Restaurant

Contact Information for Business Card

This is traditional Korean food restaurant that targets university students during lunch and Korean business travelers at dinner.

Font styles to use
Sans Serif

Requirements
Must have
• Must have my logo.

```html
<!DOCTYPE html>
<html lang="en">
<head>
<meta charset="utf-8">
<title>Nal Som — Business Card</title>
<link rel="stylesheet" href="https://fonts.googleapis.com/css2?family=Josefin+Sans:ital,wght@0,300;0,400;0,700;1,300&family=Noto+Sans+KR:wght@400&display=swap">
<style>
  :root {
    --mint: #9dcbb5;
    --ink: #111111;
    --paper: #ffffff;
    --band-text: #cfcfcf;
    --soft-ink: #2a2a2a;
    --label: #ffffff;
  }
  * { margin: 0; padding: 0; box-sizing: border-box; }
  html, body { width: 900px; height: 1200px; overflow: hidden; }
  body {
    background: var(--mint);
    font-family: "Josefin Sans", "Noto Sans KR", sans-serif;
    position: relative;
  }
  .side-label {
    position: absolute; left: 70px;
    font-size: 30px; font-weight: 300; font-style: italic;
    color: var(--label); letter-spacing: 1px;
  }
  .card {
    position: absolute; left: 70px; width: 760px; height: 440px;
    overflow: hidden;
  }
  /* FRONT */
  .card-front { top: 110px; background: var(--paper); color: var(--ink); }
  .tagline {
    position: absolute; top: 70px; width: 100%; text-align: center;
    font-size: 34px; font-weight: 400; letter-spacing: 5px;
  }
  .name-row {
    position: absolute; top: 150px; left: 0; width: 100%; height: 140px;
    display: flex; align-items: center; justify-content: center; gap: 26px;
  }
  .rule-pair { width: 120px; height: 82px; border-top: 2px solid var(--ink); border-bottom: 2px solid var(--ink); }
  .name-lockup { display: flex; align-items: center; gap: 20px; }
  .name-mark { width: 110px; height: 110px; border-radius: 50%; background: var(--ink); }
  .brand-name { font-size: 62px; font-weight: 700; line-height: 1; padding-top: 8px; white-space: nowrap; }
  .hours-band {
    position: absolute; top: 340px; left: 0; width: 100%; height: 46px;
    background: var(--ink); color: var(--band-text);
    display: flex; align-items: center; justify-content: center;
    font-size: 19px; font-weight: 300; letter-spacing: 3px; padding-top: 4px;
  }
  /* BACK */
  .card-back { top: 650px; background: var(--ink); color: var(--paper); }
  .utensil-art {
    position: absolute; left: 0; top: 0; width: 270px; height: 100%;
    background: linear-gradient(90deg, #3a3a3a 0%, #1d1d1d 100%);
    display: flex; align-items: center; justify-content: center;
  }
  .utensil-art .brand-name { font-size: 44px; color: var(--paper); }
  .contact-list {
    position: absolute; left: 320px; top: 70px;
    list-style: none; display: flex; flex-direction: column; gap: 48px;
  }
  .contact-item { display: flex; align-items: flex-start; gap: 24px; }
  .contact-icon { width: 30px; height: 34px; flex: none; }
  .contact-text { font-size: 22px; font-weight: 300; line-height: 1.2; padding-top: 4px; }
  .contact-text .ko { font-family: "Noto Sans KR", sans-serif; font-weight: 400; }
  .contact-text em { font-style: italic; }
</style>
</head>
<body>
  <div class="side-label" style="top:55px">FRONT</div>
  <section class="card card-front">
    <p class="tagline">· korean homecooking ·</p>
    <div class="name-row">
      <span class="rule-pair"></span>
      <div class="name-lockup">
        <span class="name-mark"></span>
        <span class="brand-name">Nal Som</span>
      </div>
      <span class="rule-pair"></span>
    </div>
    <div class="hours-band">• OPEN MON - SAT • 10AM - 8PM •</div>
  </section>

  <div class="side-label" style="top:595px">BACK</div>
  <section class="card card-back">
    <div class="utensil-art" role="img" aria-label="White spoon and chopsticks illustration">
      <span class="brand-name">Nal Som</span>
    </div>
    <ul class="contact-list">
      <li class="contact-item">
        <svg class="contact-icon" viewBox="0 0 30 34" aria-hidden="true"><path d="M15 2a10 10 0 0 0-10 10c0 8 10 20 10 20s10-12 10-20A10 10 0 0 0 15 2z" fill="#fff"/><circle cx="15" cy="12" r="4" fill="#111"/></svg>
        <p class="contact-text"><span class="ko">늘찬</span> <em>Nal Som</em><br>478 Harwell Rd.<br>Clarksville, TN 37118</p>
      </li>
      <li class="contact-item">
        <svg class="contact-icon" viewBox="0 0 30 34" aria-hidden="true"><circle cx="15" cy="17" r="13" fill="none" stroke="#fff" stroke-width="2"/><path d="M10 10c-1 4 4 12 9 14l2-3-3-2-2 2c-2-1-4-4-5-6l2-1-1-4z" fill="#fff"/></svg>
        <p class="contact-text">931-617-3084</p>
      </li>
      <li class="contact-item">
        <svg class="contact-icon" viewBox="0 0 30 34" aria-hidden="true"><rect x="7" y="2" width="16" height="30" rx="2" fill="none" stroke="#fff" stroke-width="2"/><line x1="12" y1="28" x2="18" y2="28" stroke="#fff" stroke-width="2"/></svg>
        <p class="contact-text">Mark Yoon • <em>Owner</em><br>931-608-2913</p>
      </li>
    </ul>
  </section>
</body>
</html>
```